Two Versions of a Business Card for a Lawyer

Summary: I need a logo and a business card. The business card is two-sided and comes in two versions. One version is conservative, the other is slightly different with one or more pink embellishments in the logo or somewhere else in the business card.
I'm about to start off as a sole practitioner in criminal and immigration law. I'll largely be working with marginalised communities and in areas of social justice. One of my main focuses will be gendered violence, I'm hoping to specialise my practice towards representing victims of domestic and sexual violence and sex workers. I want a business card which would attract this clientele and make them feel safe to speak with me. I'd also like it to communicate a sense of hope.
However, the business card still has to be very conservative as the legal profession is very stuffy. So I was thinking of having two versions of the same card, one would be very straight forward while the other would have a **pink embellishment** or perhaps several. For example, if the scales of justice were used in the design, maybe the second version would have a pink flower about to bloom on the scale somewhere. Or maybe it's my logo that is different and pink.
While both designs have to be pretty conservative, I still want it to give off a sense that I'm alternative and think outside the box. With lawyers, I think a little bit of deviation goes a long way (less is more).
As far as colour goes (other than the pink embellishment), I was thinking something monochromatic, probably black and white but I am open to considering more colours. I personally love colour, and would love to use more colour, but am hesitant because of the nature of the profession. If you can find a way to use more colour while keeping it conservative and letting the pink pop, I'd be pretty pleased.
In general, I would prefer a clean simplistic design and logo. It should be immediately obvious that I'm a lawyer just by glancing at the card. I'm open to symbols of law, like the scales of justice or lady justice or something else. However, I don't want it to be the same as everyone else's.
Eventually, the design/style should be easy to recreate in the form of a website.
As far as the logo goes, it would probably use a circle as my last name starts with the letter "O". It can be very simple, with just my name and "Barrister & Solicitor". I don't currently have a logo, but the winning designer will be invited to provide a separate file for just the logo for an additional fee (I think it was CA$99). (Please ignore the uploaded logo file, it just wouldn't let me continue without uploading something).
As for the information that should go into the card, I'm still finalizing my address and phone number. So please use a placeholder for now.
Target Market(s)
Women, victims of sexual or domestic violence, refugees, people in need of legal services
Industry/Entity Type
Lawyer
Contact Information for Business Card
Maren Vickery
Barrister & Solicitor
LL.M., B.A., M.S.W.
Criminal & Immigration Law
Street address
Larkmoor, NR
Postal Code
Phone number
Fax number
Email
Logo Text
Maren Vickery, Barrister & Solicitor
Requirements
Must have
- Two versions
- One with pink
- Simplistic
Nice to have
- Maybe more colour
Should not have
- Not too conservative
- Not too predictable

```html
<!DOCTYPE html>
<html lang="en">
<head>
<meta charset="utf-8">
<title>Maren Vickery – Business Cards</title>
<link rel="stylesheet" href="https://fonts.googleapis.com/css2?family=Lato:wght@400;700&family=Source+Sans+3:wght@400&display=swap">
<style>
  :root {
    --bg: #ecebea;
    --ink: #1c1c1c;
    --pink: #d6399b;
    --paper: #ffffff;
    --black-card: #1a1a1a;
    --white: #ffffff;
  }
  * { box-sizing: border-box; margin: 0; padding: 0; }
  html, body { width: 1200px; height: 960px; overflow: hidden; }
  body {
    background: var(--bg);
    font-family: "Lato", sans-serif;
    color: var(--ink);
    position: relative;
  }

  /* Brand lockup */
  .brand {
    position: absolute; left: 48px; top: 56px;
    display: flex; align-items: center; gap: 18px;
    font-family: "Source Sans 3", sans-serif;
  }
  .brand-ring {
    width: 100px; height: 100px; border-radius: 50%;
    border: 7px solid var(--ink);
  }
  .brand-name { font-size: 42px; line-height: 1; font-weight: 400; }
  .brand-role { font-size: 19px; margin-top: 8px; font-weight: 400; }

  /* Cards */
  .card {
    position: absolute; width: 420px; height: 240px;
    overflow: hidden;
    box-shadow: 0 14px 26px rgba(0,0,0,.22);
  }
  .card-back-pink { left: 150px; top: 250px; background: var(--pink); }
  .card-front-pink { left: 630px; top: 230px; background: var(--paper); border-bottom: 8px solid var(--pink); }
  .card-front-black { left: 150px; top: 580px; background: var(--paper); border-bottom: 8px solid var(--black-card); }
  .card-back-black { left: 630px; top: 600px; background: var(--black-card); }

  /* Back faces */
  .back-halo {
    position: absolute; left: 140px; top: 10px;
    width: 220px; height: 220px; border-radius: 50%;
    border: 22px solid rgba(255,255,255,.12);
  }
  .back-lockup {
    position: absolute; left: 70px; top: 80px;
    display: flex; align-items: center; gap: 14px; color: var(--white);
  }
  .back-ring {
    width: 66px; height: 66px; border-radius: 50%;
    border: 5px solid var(--white);
  }
  .back-name { font-size: 30px; line-height: 1; }
  .back-role { font-size: 13px; margin-top: 5px; }

  /* Front faces */
  .card-front-pink { --accent: var(--pink); }
  .card-front-black { --accent: var(--ink); }
  .front-ring {
    position: absolute; right: 24px; top: 18px;
    width: 96px; height: 96px; border-radius: 50%;
    border: 7px solid var(--accent);
  }
  .front-title {
    position: absolute; left: 24px; top: 94px;
    padding-left: 14px; border-left: 8px solid var(--accent);
  }
  .front-name { font-size: 22px; line-height: 1.05; white-space: nowrap; }
  .front-creds { font-size: 11px; color: var(--accent); margin-left: 4px; }
  .front-role { font-size: 12px; color: var(--accent); margin-top: 2px; }

  .contact {
    position: absolute; left: 46px; top: 140px;
    list-style: none; font-size: 10.5px; line-height: 1.25;
  }
  .contact li { display: flex; align-items: flex-start; gap: 8px; }
  .contact svg { width: 10px; height: 10px; margin-top: 2px; fill: var(--accent); flex: none; }
</style>
</head>
<body>

  <header class="brand">
    <div class="brand-ring"></div>
    <div>
      <div class="brand-name">Maren Vickery</div>
      <div class="brand-role">Barrister &amp; Solicitor</div>
    </div>
  </header>

  <section class="card card-back-pink">
    <div class="back-halo"></div>
    <div class="back-lockup">
      <div class="back-ring"></div>
      <div>
        <div class="back-name">Maren Vickery</div>
        <div class="back-role">Barrister &amp; Solicitor</div>
      </div>
    </div>
  </section>

  <section class="card card-front-pink">
    <div class="front-ring"></div>
    <div class="front-title">
      <div class="front-name">Maren Vickery<span class="front-creds">LL.M., B.A., M.S.W.</span></div>
      <div class="front-role">Barrister &amp; Solicitor</div>
    </div>
    <ul class="contact">
      <li><svg viewBox="0 0 10 10"><path d="M5 0a3.5 3.5 0 0 0-3.5 3.5C1.5 6 5 10 5 10s3.5-4 3.5-6.5A3.5 3.5 0 0 0 5 0zm0 5a1.4 1.4 0 1 1 0-2.8A1.4 1.4 0 0 1 5 5z"/></svg><span>Street address<br>Larkmoor, NR<br>Postal Code</span></li>
      <li><svg viewBox="0 0 10 10"><path d="M1 3c0-1 1-2 2-2l1 2-1 1c.5 1 1.5 2 2.5 2.5l1-1 2 1c0 1-1 2-2 2C4 8.5 1.5 6 1 3z"/></svg><span>Phone number</span></li>
      <li><svg viewBox="0 0 10 10"><rect x="2" y="1" width="6" height="3"/><rect x="0.5" y="4" width="9" height="5" rx="1"/></svg><span>Fax number</span></li>
      <li><svg viewBox="0 0 10 10"><path d="M0 2h10v6H0z M0 2l5 3.5L10 2"/></svg><span>Email</span></li>
    </ul>
  </section>

  <section class="card card-front-black">
    <div class="front-ring"></div>
    <div class="front-title">
      <div class="front-name">Maren Vickery<span class="front-creds">LL.M., B.A., M.S.W.</span></div>
      <div class="front-role">Barrister &amp; Solicitor</div>
    </div>
    <ul class="contact">
      <li><svg viewBox="0 0 10 10"><path d="M5 0a3.5 3.5 0 0 0-3.5 3.5C1.5 6 5 10 5 10s3.5-4 3.5-6.5A3.5 3.5 0 0 0 5 0zm0 5a1.4 1.4 0 1 1 0-2.8A1.4 1.4 0 0 1 5 5z"/></svg><span>Street address<br>Larkmoor, NR<br>Postal Code</span></li>
      <li><svg viewBox="0 0 10 10"><path d="M1 3c0-1 1-2 2-2l1 2-1 1c.5 1 1.5 2 2.5 2.5l1-1 2 1c0 1-1 2-2 2C4 8.5 1.5 6 1 3z"/></svg><span>Phone number</span></li>
      <li><svg viewBox="0 0 10 10"><rect x="2" y="1" width="6" height="3"/><rect x="0.5" y="4" width="9" height="5" rx="1"/></svg><span>Fax number</span></li>
      <li><svg viewBox="0 0 10 10"><path d="M0 2h10v6H0z M0 2l5 3.5L10 2"/></svg><span>Email</span></li>
    </ul>
  </section>

  <section class="card card-back-black">
    <div class="back-halo"></div>
    <div class="back-lockup">
      <div class="back-ring"></div>
      <div>
        <div class="back-name">Maren Vickery</div>
        <div class="back-role">Barrister &amp; Solicitor</div>
      </div>
    </div>
  </section>

</body>
</html>
```